One page sales fact sheet for data consultancy company

We need a serious and professional looking 1-page fact sheet that we want to send over to potential clients via email.
The upper part should consists of a header, the client logo and 3 charts.
(1 chart with 5 datapoints / 1 chart with 3 bubbles and percentage in it, 1 chart with numbers and text)
In the lower part there should be some text description about our company and a big chart consisting of a table (see drawing).
See attached drawing to get a better understanding of the whole idea.
The fact sheet should be catchy but professional in the same way.
Colors your choice but classic, i.e. black/white/grey/blue
The contest winner can expect more work from us based on the winning design.
*Please note that the logo reflects our original logo style but is not our
actual company name for privacy reasons

```html
<!DOCTYPE html>
<html lang="en">
<head>
<meta charset="utf-8">
<title>Market Analysis Fact Sheet</title>
<link href="https://fonts.googleapis.com/css2?family=Poppins:wght@500;600;700;800&family=Arimo:wght@400&display=swap" rel="stylesheet">
<style>
  :root {
    --page: #f6f6f7;
    --panel: #ececee;
    --lower-band: #e9e9eb;
    --brand-blue: #1b70b9;
    --navy: #1d4d80;
    --stat-strong: #4b7bbf;
    --stat-mid: #5f89c6;
    --stat-soft: #a3b9e0;
    --stat-pale: #c5d2ec;
    --bar-1: #c5d2ec;
    --bar-2: #9eb3dc;
    --bar-3: #7898cf;
    --bar-4: #4b7bbf;
    --ring-grey: #b5b5b8;
    --ink: #111111;
    --white: #ffffff;
  }
  * { box-sizing: border-box; margin: 0; padding: 0; }
  html, body { width: 947px; height: 1200px; overflow: hidden; background: var(--page); }
  .sheet { position: relative; width: 947px; height: 1200px; background: var(--page); font-family: "Poppins", sans-serif; }

  .title-bar { position: absolute; left: 0; top: 65px; width: 538px; height: 61px; background: var(--brand-blue);
    display: flex; align-items: center; padding-left: 42px; }
  .title-bar h1 { color: var(--white); font-size: 35px; font-weight: 700; letter-spacing: 6.5px; }

  .brand-name { position: absolute; left: 660px; top: 62px; width: 230px; height: 70px; display: flex; align-items: center;
    justify-content: center; font-size: 54px; font-weight: 800; color: var(--ink); letter-spacing: 1px; }

  .panel-tab { position: absolute; top: 196px; height: 45px; background: var(--navy); border-radius: 24px 24px 0 0;
    color: var(--white); font-size: 25px; font-weight: 600; letter-spacing: 2.5px; display: flex; align-items: center; justify-content: center; }
  .panel-tab.left { left: 49px; width: 382px; }
  .panel-tab.right { left: 509px; width: 382px; }
  .chart-panel { position: absolute; top: 240px; height: 307px; background: var(--panel); }
  .chart-panel.left { left: 23px; width: 443px; }
  .chart-panel.right { left: 481px; width: 442px; }
  .chart-panel svg { display: block; }

  .stat { position: absolute; height: 69px; display: flex; align-items: center; padding-left: 28px;
    clip-path: polygon(0 0, calc(100% - 22px) 0, 100% 22px, 100% 100%, 0 100%); letter-spacing: 2px; font-size: 22px; font-weight: 500; }
  .stat strong { font-size: 30px; font-weight: 700; margin-right: 10px; letter-spacing: 2px; }
  .stat .icon { position: absolute; right: 22px; top: 50%; transform: translateY(-50%); }
  .stat.vendors { left: 23px; top: 561px; width: 443px; background: var(--stat-strong); color: var(--white); }
  .stat.availability { left: 23px; top: 643px; width: 443px; background: var(--stat-mid); color: var(--white); }
  .stat.products { left: 481px; top: 561px; width: 442px; background: var(--stat-soft); color: var(--navy); }
  .stat.sales { left: 481px; top: 643px; width: 442px; background: var(--stat-pale); color: var(--navy); }
  .stat.products strong, .stat.sales strong { font-size: 36px; }

  .company-text { position: absolute; left: 23px; top: 734px; width: 900px; font-family: "Arimo", sans-serif;
    font-size: 15.6px; line-height: 18.8px; color: var(--ink); }

  .lower-band { position: absolute; left: 0; top: 917px; width: 947px; height: 283px; background: var(--lower-band); }
  .level-bar { position: absolute; left: 23px; height: 50px; display: flex; align-items: center; padding-left: 34px;
    font-size: 26px; font-weight: 600; letter-spacing: 3px; }
  .level-bar.competitors { top: 957px; width: 326px; background: var(--bar-1); color: var(--navy); }
  .level-bar.user { top: 1015px; width: 434px; background: var(--bar-2); color: var(--navy); }
  .level-bar.entity { top: 1072px; width: 580px; background: var(--bar-3); color: var(--white); }
  .level-bar.personal { top: 1129px; width: 734px; background: var(--bar-4); color: var(--white); }
</style>
</head>
<body>
<main class="sheet">
  <header>
    <div class="title-bar"><h1>MARKET ANALYSIS</h1></div>
    <div class="brand-name">NORVEN</div>
  </header>

  <div class="panel-tab left">PRODUCT TYPES</div>
  <section class="chart-panel left" aria-label="Product types trend chart">
    <svg width="443" height="307" viewBox="0 0 443 307" font-family="Poppins, sans-serif" font-size="11" fill="#222">
      <line x1="101" y1="46" x2="101" y2="241" stroke="#1b70b9" stroke-width="4"/>
      <line x1="99" y1="241" x2="360" y2="241" stroke="#1b70b9" stroke-width="4"/>
      <polyline points="127,172 150,194 190,144 210,162 345,77" fill="none" stroke="#3a3a3a" stroke-width="3.5" stroke-linejoin="miter"/>
      <g text-anchor="end">
        <text x="92" y="68">50</text><text x="92" y="107">40</text><text x="92" y="148">30</text>
        <text x="92" y="187">20</text><text x="92" y="227">10</text>
      </g>
      <g text-anchor="middle">
        <text x="84" y="261">0</text><text x="133" y="261">10</text><text x="182" y="261">20</text>
        <text x="230" y="261">30</text><text x="278" y="261">40</text><text x="325" y="261">50</text>
      </g>
    </svg>
  </section>

  <div class="panel-tab right">PRODUCT TYPES</div>
  <section class="chart-panel right" aria-label="Product type share rings">
    <svg width="442" height="307" viewBox="0 0 442 307" font-family="Poppins, sans-serif" font-weight="700" font-size="19" text-anchor="middle">
      <g transform="translate(131,83)">
        <circle r="54" fill="#f4f4f5"/><circle r="50" fill="#e7e7e9"/>
        <circle r="34" fill="none" stroke="var(--ring-grey)" stroke-width="13"/>
        <circle r="34" fill="none" stroke="var(--brand-blue)" stroke-width="13" stroke-dasharray="21.4 192" transform="rotate(-90)"/>
        <circle r="27.5" fill="#ffffff"/><text y="7">10%</text>
      </g>
      <g transform="translate(304,83)">
        <circle r="54" fill="#f4f4f5"/><circle r="50" fill="#e7e7e9"/>
        <circle r="34" fill="none" stroke="var(--ring-grey)" stroke-width="13"/>
        <circle r="34" fill="none" stroke="var(--brand-blue)" stroke-width="13" stroke-dasharray="42.7 192" transform="rotate(-60)"/>
        <circle r="27.5" fill="#ffffff"/><text y="7">20%</text>
      </g>
      <g transform="translate(131,221)">
        <circle r="54" fill="#f4f4f5"/><circle r="50" fill="#e7e7e9"/>
        <circle r="34" fill="none" stroke="var(--ring-grey)" stroke-width="13"/>
        <circle r="34" fill="none" stroke="var(--brand-blue)" stroke-width="13" stroke-dasharray="85.5 192" transform="rotate(120)"/>
        <circle r="27.5" fill="#ffffff"/><text y="7">40%</text>
      </g>
      <g transform="translate(304,221)">
        <circle r="54" fill="#f4f4f5"/><circle r="50" fill="#e7e7e9"/>
        <circle r="34" fill="none" stroke="var(--ring-grey)" stroke-width="13"/>
        <circle r="34" fill="none" stroke="var(--brand-blue)" stroke-width="13" stroke-dasharray="64 192" transform="rotate(20)"/>
        <circle r="27.5" fill="#ffffff"/><text y="7">30%</text>
      </g>
    </svg>
  </section>

  <div class="stat vendors"><strong>20</strong>VENDORS
    <svg class="icon" width="42" height="50" viewBox="0 0 42 50" fill="none" stroke="#ffffff" stroke-width="2.2" stroke-linecap="round" stroke-linejoin="round">
      <circle cx="18" cy="13" r="10"/><path d="M2 47v-6a13 13 0 0 1 13-13h6"/><path d="M24 40l5 5 10-11"/>
    </svg>
  </div>
  <div class="stat products"><strong>150</strong>PRODUCTS
    <svg class="icon" width="46" height="46" viewBox="0 0 46 46" fill="none" stroke="#1d4d80" stroke-width="3">
      <rect x="3" y="3" width="9" height="9"/><rect x="18.5" y="3" width="9" height="9"/><rect x="34" y="3" width="9" height="9"/>
      <rect x="3" y="18.5" width="9" height="9"/><rect x="18.5" y="18.5" width="9" height="9"/><rect x="34" y="18.5" width="9" height="9"/>
      <rect x="3" y="34" width="9" height="9"/><rect x="18.5" y="34" width="9" height="9"/><rect x="34" y="34" width="9" height="9"/>
    </svg>
  </div>
  <div class="stat availability"><strong>350.000</strong>AVALIABILITY
    <svg class="icon" width="50" height="46" viewBox="0 0 50 46" fill="none" stroke="#ffffff" stroke-width="2.2" stroke-linecap="round" stroke-linejoin="round">
      <path d="M2 4h7l6 26h26l4-16"/><path d="M12 20h30"/><circle cx="18" cy="39" r="3.5"/><circle cx="37" cy="39" r="3.5"/>
      <path d="M26 10l5 5 12-13"/>
    </svg>
  </div>
  <div class="stat sales"><strong>40</strong>MLN. IN SALES
    <svg class="icon" width="40" height="50" viewBox="0 0 40 50" fill="none" stroke="#1d4d80" stroke-width="2.2" stroke-linejoin="round">
      <path d="M3 9h26l8 8v31H3z"/><path d="M9 3h26l4 4"/><path d="M29 9v8h8"/>
      <text x="20" y="39" text-anchor="middle" font-family="Arimo, sans-serif" font-size="22" fill="#1d4d80" stroke="none">$</text>
    </svg>
  </div>

  <section class="company-text">
    <p>Lorem ipsum dolor sit amet, consectetuer adipiscing elit, sed diam nonummy nibh euismod tincidunt ut laoreet dolore magna aliquam erat volutpat. Ut wisi enim ad minim veniam, quis nostrud exerci tation ullamcorper suscipit lobortis nisl ut aliquip ex ea commodo consequat. Duis autem vel eum</p>
    <p>Lorem ipsum dolor sit amet, consectetuer adipiscing elit, sed diam nonummy nibh euismod tincidunt ut laoreet dolore magna aliquam erat volutpat. Ut wisi enim ad minim veniam, quis nostrud exerci tation ullamcorper suscipit lobortis nisl ut aliquip ex ea commodo consequat. Duis autem vel eum Lorem ipsum dolor sit amet, consectetuer adipiscing elit, sed diam nonummy nibh euismod tincidunt ut laoreet dolore magna aliquam erat volutpat. Ut wisi enim ad minim veniam, quis nostrud exerci tation ullamcorper suscipit lobortis nisl ut aliquip ex ea commodo consequat. Duis autem vel eum</p>
  </section>

  <section class="lower-band" aria-hidden="true"></section>
  <div class="level-bar competitors">COMPETITORS</div>
  <div class="level-bar user">USER LEVEL</div>
  <div class="level-bar entity">ENTITY LEVEL</div>
  <div class="level-bar personal">PERSONAL LEVEL</div>
</main>
</body>
</html>
```